Kem7Dex Letterhead

Need a new letterhead for my law firm.
IDENTIFYING INFORMATION BELOW:
Ansel T Brightwater III
Attorney at Law
Address: 4832 Tillbury Rd, Ste 250, Dallas, TX 75204
Phone: 866-402-7183
Fax: 469-583-0271
Email: kem@kem7dex.example
Website: www.kem7dex.example

Colors
0054AA
0677BA
7BADD7
CADEEF
E8F1F8

Requirements
Must have
• Logo needs to be on the letterhead, along with identifying information which is included in the project description.

```html
<!DOCTYPE html>
<html lang="en">
<head>
<meta charset="utf-8">
<title>Kem7Dex Letterhead</title>
<link href="https://fonts.googleapis.com/css2?family=Montserrat:wght@400;500;700&display=swap" rel="stylesheet">
<style>
  :root {
    --stage: #1f1f1f;
    --paper: #ffffff;
    --ink: #1c1c1c;
    --ink-soft: #333333;
    --rule: #8a8a8a;
    --icon-blue: #1e8fd0;
    --blue-deep: #0054AA;
    --blue-mid: #0677BA;
    --blue-light: #1da1dc;
    --band: #151515;
  }
  * { margin: 0; padding: 0; box-sizing: border-box; }
  html, body {
    width: 1200px; height: 1059px; overflow: hidden;
    background: var(--stage);
    font-family: "Montserrat", sans-serif;
  }
  .letterhead {
    position: absolute; left: 246px; top: 29px;
    width: 707px; height: 1000px;
    background: var(--paper);
    box-shadow: 0 18px 40px rgba(0,0,0,0.55);
    color: var(--ink-soft);
  }
  .brand-name {
    position: absolute; left: 40px; top: 66px;
    font-size: 44px; font-weight: 700; letter-spacing: 4px;
    text-transform: uppercase; color: var(--ink); line-height: 1;
  }
  .contact-rule {
    position: absolute; left: 493px; top: 62px;
    width: 1px; height: 81px; background: var(--rule);
  }
  .contact {
    position: absolute; left: 511px; top: 58px;
    font-size: 12.7px; line-height: 17.5px; color: var(--ink-soft);
    list-style: none;
  }
  .contact .address { margin-bottom: 4px; }
  .contact li { display: flex; align-items: center; gap: 5px; }
  .contact svg { width: 11px; height: 11px; fill: var(--icon-blue); flex: none; }
  .letter {
    position: absolute; left: 41px; top: 242px; width: 626px;
    font-size: 13.3px; line-height: 20.3px; color: var(--ink-soft);
    letter-spacing: 0.1px;
  }
  .recipient { line-height: 20.4px; }
  .letter p { text-align: justify; }
  .p-second { margin-top: 21px; }
  .p-third { margin-top: 18px; }
  .closing { margin-top: 12px; }
  .signature {
    width: 128px; height: 54px; margin-top: 14px;
    background: linear-gradient(90deg, #efefef, #f7f7f7);
  }
  .footer {
    position: absolute; left: 0; bottom: 0; width: 707px; height: 37px;
  }
  .footer svg { display: block; }
  .web {
    position: absolute; left: 396px; top: 0; width: 256px; height: 25px;
    display: flex; align-items: center; justify-content: center; gap: 6px;
    color: #ffffff; font-size: 14.5px; font-weight: 500; letter-spacing: 0.2px;
    white-space: nowrap;
  }
  .web svg { width: 12px; height: 12px; fill: #1a1a1a; }
</style>
</head>
<body>
  <main class="letterhead">
    <header>
      <div class="brand-name">Kem7Dex</div>
      <div class="contact-rule"></div>
      <ul class="contact">
        <li class="address">4832 Tillbury Rd, Ste<br>250, Dallas, TX 75204</li>
        <li>
          <svg viewBox="0 0 24 24" aria-hidden="true"><path d="M6.6 10.8a15.1 15.1 0 0 0 6.6 6.6l2.2-2.2a1 1 0 0 1 1-.25 11.4 11.4 0 0 0 3.6.57 1 1 0 0 1 1 1V20a1 1 0 0 1-1 1A17 17 0 0 1 3 4a1 1 0 0 1 1-1h3.5a1 1 0 0 1 1 1c0 1.25.2 2.45.57 3.57a1 1 0 0 1-.25 1z"/></svg>
          866-402-7183
        </li>
        <li>
          <svg viewBox="0 0 24 24" aria-hidden="true"><path d="M6 2h12v5H6zM3 8h18a1 1 0 0 1 1 1v8h-4v5H6v-5H2V9a1 1 0 0 1 1-1zm5 8v4h8v-4z"/></svg>
          469-583-0271
        </li>
        <li>
          <svg viewBox="0 0 24 24" aria-hidden="true"><path d="M2 5h20v14H2zm2 2v.5l8 5.5 8-5.5V7l-8 5.5z"/></svg>
          kem@kem7dex.example
        </li>
      </ul>
    </header>

    <section class="letter">
      <div class="recipient">
        Mr/s<br>
        First Name and Last Name<br>
        Company Name<br>
        Address
      </div>
      <p>Lorem Ipsum is simply dummy text of the printing and typesetting industry. Lorem Ipsum has been the industry's standard dummy text ever since the 1500s, when an unknown printer took a galley of type and scrambled it to make a type specimen book. It has survived not only five centuries, but also the leap into electronic typesetting, remaining essentially unchanged. It was popularised in the 1960s.</p>
      <p class="p-second">he standard chunk of Lorem Ipsum used since the 1500s is reproduced below for those interested. Sections 1.10.32 and 1.10.33 from "de Finibus Bonorum et Malorum" by Tullio Varn are also reproduced in their exact original form, accompanied by English versions from the 1914 translation by J. Pellworth. Lorem ipsum dolor sit amet, consectetur adipiscing elit, sed do eiusmod tempor incididunt ut labore et dolore magna aliqua.</p>
      <p class="p-third">It is a long established fact that a reader will be distracted by the readable content of a page when looking at its layout. The point of using Lorem Ipsum is that it has a more-or-less normal distribution of letters, as opposed to using 'Content here, content here', making it look like readable English. Many desktop publishing packages and web page editors now .</p>
      <div class="closing">Your Sincerely,</div>
      <div class="signature" role="img" aria-label="Handwritten signature of the sender"></div>
    </section>

    <footer class="footer">
      <svg width="707" height="37" viewBox="0 0 707 37" aria-hidden="true">
        <defs>
          <linearGradient id="tab-blue" x1="0" x2="1" y1="0" y2="0">
            <stop offset="0" stop-color="#0054AA"/>
            <stop offset="0.55" stop-color="#0677BA"/>
            <stop offset="1" stop-color="#1da1dc"/>
          </linearGradient>
        </defs>
        <rect x="0" y="25" width="707" height="12" fill="#151515"/>
        <polygon points="358,37 394,25 656,25 684,37" fill="#ffffff"/>
        <polygon points="368,37 403,0 648,0 675,37" fill="url(#tab-blue)"/>
      </svg>
      <div class="web">
        <svg viewBox="0 0 24 24" aria-hidden="true"><circle cx="12" cy="12" r="10"/><path d="M7 7c2 0 3 1 3 3s2 2 1 4-2 2-2 4M16 4c-1 2 0 3 2 3s2 3 1 5" stroke="#ffffff" stroke-width="1.6" fill="none"/></svg>
        www.kem7dex.example
      </div>
    </footer>
  </main>
</body>
</html>
```